Maple Sprout Menu (Vegetarian Restaurant Concept)

Maple Sprout is a new concept fast casual restaurant
renders are attached so you can see the style of restaurant
Maple Sprowt is a vibrant and modern Vegetarian fast casual restaurant concept that mixes fresh food, energy, great décor, and a comfortable, welcoming atmosphere to provide a memorable and all Vegetarian dining experience.
Our Mission is to be top of mind when consumers think Vegetarian food!
Target Market(s)
the menu is vegetarian and appeals to a broad demographic in USA
Colors
Designer to choose colors to be used in the design.
Requirements
Must have
- well colored and well laid out menu - should not be cartoonish
Nice to have
- For Phots please use the shots in this file:
- https://www.filecrate-example.net/sh/kq7trm2wzl4pnad/BBBxT_qPwLdRNVoE_KMS_Tb?dl=0
- note these are untouched and you are free to change as needed
Should not have
- Should not be cartoonish - nor kives, forks etc in the design

```html
<!DOCTYPE html>
<html lang="en">
<head>
<meta charset="utf-8">
<title>Maple Sprowt – Vegetarian Restaurant Menu</title>
<link href="https://fonts.googleapis.com/css2?family=Alegreya+Sans:wght@300;400;700&family=Open+Sans:wght@700&family=Sriracha&display=swap" rel="stylesheet">
<style>
  :root{
    --page:#ffffff;
    --panel:#2b2b2b;
    --ink:#ffffff;
    --accent:#f0923e;
    --leaf:#7dc242;
    --cream:#efeee6;
    --dark-text:#2b2b2b;
  }
  *{box-sizing:border-box;margin:0;padding:0}
  html,body{width:1200px;height:1200px;overflow:hidden;background:var(--page)}
  .canvas{position:relative;width:1200px;height:1200px;font-family:"Alegreya Sans",sans-serif;color:var(--ink)}
  .sheet{position:absolute;background:var(--panel)}
  .sheet--outside{left:220px;top:32px;width:767px;height:543px}
  .sheet--inside{left:219px;top:617px;width:772px;height:547px}
  .photo-band{position:absolute;display:flex}
  .photo-band .photo{flex:1;height:100%}
  .frame{position:absolute;pointer-events:none}
  .frame .line{fill:none;stroke:var(--ink);stroke-width:1.3}
  .frame .dash{fill:none;stroke:var(--ink);stroke-width:.8;stroke-dasharray:4 3}
  .heading{position:absolute;font-family:"Open Sans",sans-serif;font-weight:700;color:var(--accent);text-align:center;font-size:18px;letter-spacing:.3px;line-height:1.35}
  .row{position:absolute;display:flex;justify-content:space-between;align-items:flex-start;font-weight:300}
  .row .name{flex:1;line-height:1.15;padding-right:8px}
  .row .price{flex:none;text-align:right}
  .row .desc{display:block;color:var(--accent);font-size:6px;line-height:1.35;margin-top:2px;max-width:190px}
  .row--small{font-size:10px}
  .row--small .name{line-height:1.25}
  .row--large{font-size:13px}
  .about{position:absolute;left:495px;top:72px;width:207px;font-size:10.2px;font-weight:300;line-height:1.25;text-align:justify}
  .diamond{position:absolute;transform:rotate(45deg);border:2px solid var(--leaf);background:radial-gradient(circle at 50% 50%,#9a8a66 0 22%,#d9d3c6 23% 36%,#ecebea 37%)}
  .address-label{position:absolute;left:564px;top:409px;width:90px;height:32px;border:1.5px solid var(--accent);border-radius:6px;font-weight:700;font-size:20px;text-align:center;line-height:29px}
  .contact{position:absolute;left:499px;width:200px;text-align:center;font-weight:300;font-size:15px;line-height:1.15}
  .menu-title{position:absolute;left:760px;top:78px;width:190px;text-align:center;font-family:"Sriracha",cursive;font-size:58px;color:var(--accent);letter-spacing:2px}
  .tag{position:absolute;left:753px;top:157px;width:206px;height:23px;border-radius:5px;background:var(--accent);color:var(--ink);font-weight:700;font-size:11px;letter-spacing:1.6px;text-align:center;line-height:23px}
  .brand{position:absolute;left:799px;top:390px;width:110px;height:110px;border-radius:50%;background:var(--cream);border:3px solid var(--accent);display:flex;align-items:center;justify-content:center;text-align:center;font-size:17px;font-weight:400;color:var(--dark-text);line-height:1.05}
  .dot-band{position:absolute;left:766px;top:512px;width:178px;height:10px;background:var(--accent);opacity:.3}
</style>
</head>
<body>
<div class="canvas">

  <!-- Outside sheet -->
  <div class="sheet sheet--outside"></div>

  <!-- Back panel: bowls & drinks -->
  <div class="photo-band" style="left:220px;top:32px;width:249px;height:85px">
    <div class="photo" role="img" aria-label="Photo of a beet salad with fresh herbs" style="background:linear-gradient(135deg,#8a2331,#4d6a2e)"></div>
    <div class="photo" role="img" aria-label="Photo of a strawberry balsamic ice cream sundae" style="background:linear-gradient(135deg,#ebe5de,#b5393a)"></div>
  </div>
  <div class="photo-band" style="left:220px;top:483px;width:249px;height:83px">
    <div class="photo" role="img" aria-label="Photo of a green salad with avocado and almonds" style="background:linear-gradient(135deg,#5f7c3b,#cdc6ad)"></div>
    <div class="photo" role="img" aria-label="Photo of a vegetable wrap" style="background:linear-gradient(135deg,#ece4d6,#cfc2a6)"></div>
  </div>
  <svg class="frame" style="left:220px;top:32px" width="249" height="543" viewBox="0 0 249 543">
    <path class="line" d="M22,6 H227 A16 16 0 0 0 243,22 V521 A16 16 0 0 0 227,537 H22 A16 16 0 0 0 6,521 V22 A16 16 0 0 0 22,6 Z"/>
    <rect class="dash" x="12" y="12" width="225" height="519"/>
  </svg>

  <div class="heading" style="left:220px;top:126px;width:249px">BOWLS</div>
  <div class="row row--small" style="left:246px;top:163px;width:195px"><span class="name">Roasted vegetable, and<br>spinach bowl</span><span class="price">00</span></div>
  <div class="row row--small" style="left:246px;top:201px;width:195px"><span class="name">Sugar Snap Pea and Carrot<br>Soba Noodles</span><span class="price">00</span></div>
  <div class="row row--small" style="left:246px;top:237px;width:195px"><span class="name">Whole grain and vegetable<br>buddha bowl</span><span class="price">00</span></div>
  <div class="row row--small" style="left:246px;top:276px;width:195px"><span class="name">Orange and Pistacio Quinoa</span><span class="price">00</span></div>

  <div class="heading" style="left:220px;top:349px;width:249px">DRINKS</div>
  <div class="row row--small" style="left:246px;top:385px;width:195px"><span class="name">Frouit Juice</span><span class="price">00</span></div>
  <div class="row row--small" style="left:246px;top:413px;width:195px"><span class="name">Frouit Shake</span><span class="price">00</span></div>

  <!-- Middle panel: about & address -->
  <svg class="frame" style="left:469px;top:32px" width="259" height="543" viewBox="0 0 259 543">
    <path class="line" d="M22,6 H237 A16 16 0 0 0 253,22 V521 A16 16 0 0 0 237,537 H22 A16 16 0 0 0 6,521 V22 A16 16 0 0 0 22,6 Z"/>
    <rect class="dash" x="12" y="12" width="235" height="519"/>
  </svg>
  <p class="about">Maple Sprowt is a vibrant and modern Vegetarian fast casual restaurant concept that mixes fresh food, energy, great décor, and a comfortable, welcoming atmosphere to provide a memorable and all Vegetarian dining experience.</p>

  <div class="diamond" role="img" aria-label="Photo of a bowl of beet greens" style="left:572px;top:181px;width:66px;height:66px"></div>
  <div class="diamond" role="img" aria-label="Photo of a vegetable toast" style="left:517px;top:237px;width:66px;height:66px"></div>
  <div class="diamond" role="img" aria-label="Photo of a green bean salad" style="left:627px;top:237px;width:66px;height:66px"></div>
  <div class="diamond" role="img" aria-label="Photo of a veggie burger" style="left:572px;top:290px;width:66px;height:66px"></div>

  <div class="address-label">Address</div>
  <div class="contact" style="top:451px">27 C, Orchard Lane<br>Brookfield, USA</div>
  <div class="contact" style="top:494px">+014 555 0192</div>
  <div class="contact" style="top:515px">hello@maplesprowt.example</div>

  <!-- Cover panel -->
  <svg class="frame" style="left:728px;top:32px" width="259" height="543" viewBox="0 0 259 543">
    <path class="line" d="M22,6 H237 A16 16 0 0 0 253,22 V521 A16 16 0 0 0 237,537 H22 A16 16 0 0 0 6,521 V22 A16 16 0 0 0 22,6 Z"/>
    <rect class="dash" x="12" y="12" width="235" height="519"/>
  </svg>
  <div class="menu-title">MENU</div>
  <div class="tag">VEGETARIAN RESTAURANT</div>
  <div class="diamond" role="img" aria-label="Photo of a tomato salad bowl" style="left:776px;top:227px;width:61px;height:61px"></div>
  <div class="diamond" role="img" aria-label="Photo of a veggie burger" style="left:875px;top:225px;width:61px;height:61px"></div>
  <div class="diamond" role="img" aria-label="Photo of a roasted vegetable bowl" style="left:824px;top:274px;width:61px;height:61px"></div>
  <div class="brand">Maple<br>Sprowt</div>
  <div class="dot-band" role="img" aria-label="Dotted decorative band"></div>

  <!-- Inside sheet -->
  <div class="sheet sheet--inside"></div>

  <!-- Salads & soup -->
  <div class="photo-band" style="left:219px;top:617px;width:257px;height:85px">
    <div class="photo" role="img" aria-label="Photo of an edamame and snap pea salad" style="background:linear-gradient(135deg,#3f6a2a,#8f3a2e)"></div>
    <div class="photo" role="img" aria-label="Photo of a salad with avocado and strawberries" style="background:linear-gradient(135deg,#6e8f3c,#c9c06a)"></div>
  </div>
  <div class="photo-band" style="left:219px;top:1079px;width:257px;height:85px">
    <div class="photo" role="img" aria-label="Photo of a strawberry ice cream sundae" style="background:linear-gradient(135deg,#b5393a,#ece6df)"></div>
    <div class="photo" role="img" aria-label="Photo of quesadillas with dipping sauce" style="background:linear-gradient(135deg,#e3c48e,#c99552)"></div>
  </div>
  <svg class="frame" style="left:219px;top:617px" width="257" height="547" viewBox="0 0 257 547">
    <path class="line" d="M22,6 H235 A16 16 0 0 0 251,22 V525 A16 16 0 0 0 235,541 H22 A16 16 0 0 0 6,525 V22 A16 16 0 0 0 22,6 Z"/>
    <rect class="dash" x="12" y="12" width="233" height="523"/>
  </svg>
  <div class="heading" style="left:219px;top:727px;width:257px">SALADS</div>
  <div class="row row--large" style="left:243px;top:759px;width:209px"><span class="name">Brussel Sprout Ceasar<span class="desc">Little gem romaine, toasted torn bread, parmigiano reggiano</span></span><span class="price">00</span></div>
  <div class="row row--large" style="left:243px;top:805px;width:209px"><span class="name">Heirloom Beet salad<span class="desc">Shaved chioggia beet, roasted golden beet, red quinoa, little gem, arugula, lemon vinaigrette</span></span><span class="price">00</span></div>
  <div class="row row--large" style="left:243px;top:855px;width:209px"><span class="name">Zesty Black Bean and Corn<br>Salad in lettuce cups<span class="desc">Black beans, avocado and roasted corn topped with feta crumbles in butter lettuce</span></span><span class="price">00</span></div>
  <div class="row row--large" style="left:243px;top:917px;width:209px"><span class="name">Green, Red and White<span class="desc">Spring leaves, cherry tomatoes, avocado, roasted almond and goat cheese</span></span><span class="price">00</span></div>
  <div class="heading" style="left:219px;top:980px;width:257px">SOUP</div>
  <div class="row row--large" style="left:243px;top:1018px;width:209px"><span class="name">Black Bean Chowder</span><span class="price">00</span></div>

  <!-- Toasts & dessert -->
  <div class="photo-band" style="left:484px;top:617px;width:245px;height:85px">
    <div class="photo" role="img" aria-label="Photo of black bean and corn salad in lettuce cups" style="background:linear-gradient(135deg,#9dbb55,#3a3a2a)"></div>
    <div class="photo" role="img" aria-label="Photo of a vegetable melt toast with tomatoes" style="background:linear-gradient(135deg,#e2b85a,#c9573a)"></div>
  </div>
  <div class="photo-band" style="left:484px;top:1079px;width:245px;height:85px">
    <div class="photo" role="img" aria-label="Photo of a beet and herb salad" style="background:linear-gradient(135deg,#8a2331,#4d6a2e)"></div>
    <div class="photo" role="img" aria-label="Photo of a golden beet and arugula salad" style="background:linear-gradient(135deg,#3f5f2a,#d9a93e)"></div>
  </div>
  <svg class="frame" style="left:484px;top:617px" width="245" height="547" viewBox="0 0 245 547">
    <path class="line" d="M22,6 H223 A16 16 0 0 0 239,22 V525 A16 16 0 0 0 223,541 H22 A16 16 0 0 0 6,525 V22 A16 16 0 0 0 22,6 Z"/>
    <rect class="dash" x="12" y="12" width="221" height="523"/>
  </svg>
  <div class="heading" style="left:484px;top:726px;width:245px">TOASTS</div>
  <div class="row row--large" style="left:508px;top:756px;width:197px"><span class="name">Everything Avocado toast<span class="desc">Avocado on whole grain toast with our signature spice blend</span></span><span class="price">00</span></div>
  <div class="row row--large" style="left:508px;top:799px;width:197px"><span class="name">Tomato &amp; Beet Bruschetta</span><span class="price">00</span></div>
  <div class="row row--large" style="left:508px;top:840px;width:197px"><span class="name">Vegetable Melt on garlic Toast</span><span class="price">00</span></div>
  <div class="heading" style="left:484px;top:884px;width:245px">DESSERT</div>
  <div class="row row--large" style="left:508px;top:926px;width:197px"><span class="name">Strawberry Balsamic Ice Cream<br>sundae</span><span class="price">00</span></div>
  <div class="row row--large" style="left:508px;top:971px;width:197px"><span class="name">Exotic fruit bowl</span><span class="price">00</span></div>
  <div class="row row--large" style="left:508px;top:1018px;width:197px"><span class="name">White and dark oatmeal cookie</span><span class="price">00</span></div>

  <!-- Burgers, wraps & sandwiches -->
  <div class="photo-band" style="left:737px;top:617px;width:254px;height:85px">
    <div class="photo" role="img" aria-label="Photo of a sweet potato black bean veggie burger" style="background:linear-gradient(180deg,#c4955a,#6b2f2a 60%,#d8d2c8)"></div>
    <div class="photo" role="img" aria-label="Photo of a garden veggie burger" style="background:linear-gradient(180deg,#c9a46c,#5e3d2a 60%,#d9d5cb)"></div>
  </div>
  <div class="photo-band" style="left:737px;top:1079px;width:254px;height:85px">
    <div class="photo" role="img" aria-label="Photo of a vegetable burrito" style="background:linear-gradient(135deg,#ebe3d6,#cfc4ad)"></div>
    <div class="photo" role="img" aria-label="Photo of a caesar salad with croutons and cranberries" style="background:linear-gradient(135deg,#5f8a36,#c48a3e)"></div>
  </div>
  <svg class="frame" style="left:737px;top:617px" width="254" height="547" viewBox="0 0 254 547">
    <path class="line" d="M22,6 H232 A16 16 0 0 0 248,22 V525 A16 16 0 0 0 232,541 H22 A16 16 0 0 0 6,525 V22 A16 16 0 0 0 22,6 Z"/>
    <rect class="dash" x="12" y="12" width="230" height="523"/>
  </svg>
  <div class="heading" style="left:737px;top:737px;width:254px;font-size:16px">BURGERS,<br>WRAPS &amp; SANDWICHES</div>
  <div class="row row--large" style="left:761px;top:816px;width:206px"><span class="name">Sweet Potato, black bean<br>veggie burgers with cabbage -<br>pepita slaw</span><span class="price">00</span></div>
  <div class="row row--large" style="left:761px;top:880px;width:206px"><span class="name">Roasted Sprowt, Arugula and<br>Hummus Wraps</span><span class="price">00</span></div>
  <div class="row row--large" style="left:761px;top:931px;width:206px"><span class="name">Garden Burger</span><span class="price">00</span></div>
  <div class="row row--large" style="left:761px;top:965px;width:206px"><span class="name">Beans and Greens Quesadillas<span class="desc">Greens, Mexican cheese, beans and avocado with salsa</span></span><span class="price">00</span></div>
  <div class="row row--large" style="left:761px;top:1006px;width:206px"><span class="name">Sprowt Burrito<span class="desc">greens, Mexican cheese, beans, brown rice, roasted chili corn and avocado, with ancho chili salsa, wheat tortilla</span></span><span class="price">00</span></div>

</div>
</body>
</html>
```